Roofing Contractor business card redesign

I want to redesign my business card with a fresh, eye catching concept

Target Market(s)

Residential Roofing Clients, potential employees, and subcontractors.

Industry/Entity Type

Business

Colors

Designer to choose colors to be used in the design.

Requirements
Nice to have
• I just want something that's more pleasing to the eye. You can use a combination of either / or of my logos.

```html
<!DOCTYPE html>
<html lang="en">
<head>
<meta charset="utf-8">
<title>Bright Ridge General Contractors – Business Card</title>
<link rel="stylesheet" href="https://fonts.googleapis.com/css2?family=Oswald:wght@400;500;700&display=swap">
<style>
  :root {
    --bg: #111111;
    --yellow: #fcc51c;
    --orange: #f08a1f;
    --orange-deep: #e4761a;
    --brown: #4a1a12;
    --white: #ffffff;
    --accent-text: #f08a1f;
  }
  * { box-sizing: border-box; margin: 0; padding: 0; }
  html, body { width: 1200px; height: 1000px; overflow: hidden; background: var(--bg); }
  body { font-family: "Oswald", sans-serif; position: relative; }

  .card {
    position: absolute;
    top: 350px;
    width: 520px;
    height: 300px;
    border-radius: 26px;
    overflow: hidden;
    box-shadow: 0 18px 40px rgba(0,0,0,.6);
  }

  /* Front */
  .card-front { left: 50px; background: var(--white); }
  .front-brand-zone {
    position: absolute; inset: 0 auto 0 0; width: 210px;
    background: var(--yellow);
  }
  .front-divider {
    position: absolute; top: 0; bottom: 0; left: 210px; width: 14px;
    background: var(--orange);
  }
  .front-divider::after {
    content: ""; position: absolute; top: 0; bottom: 0; left: 4px; width: 3px;
    background: var(--white);
  }
  .front-brand {
    position: absolute; left: 20px; top: 60px; width: 175px;
    display: flex; flex-direction: column; align-items: center; gap: 14px;
  }
  .brand-dot {
    width: 110px; height: 110px; border-radius: 50%;
    background: var(--brown);
  }
  .front-brand-name {
    color: var(--brown); font-weight: 700; font-size: 26px; line-height: 1.05;
    text-align: center; text-transform: none;
  }
  .front-brand-name small { display: block; font-size: 15px; font-weight: 700; }

  .contact-list {
    position: absolute; left: 250px; top: 58px; right: 20px;
    list-style: none; display: flex; flex-direction: column; gap: 22px;
  }
  .contact-row { display: flex; align-items: flex-start; gap: 12px; }
  .contact-icon {
    flex: none; width: 34px; height: 34px; border-radius: 50%;
    background: var(--brown); display: flex; align-items: center; justify-content: center;
  }
  .contact-icon svg { width: 18px; height: 18px; fill: var(--white); }
  .person-name { color: var(--brown); font-weight: 700; font-size: 24px; line-height: 1; }
  .person-title { color: var(--accent-text); font-weight: 500; font-size: 13px; line-height: 1.25; }
  .contact-text { color: var(--brown); font-weight: 500; font-size: 16px; line-height: 1.3; padding-top: 6px; }
  .contact-text .accent { color: var(--accent-text); }
  .contact-text .label { font-weight: 700; }

  /* Back */
  .card-back {
    left: 630px;
    background: linear-gradient(135deg, var(--orange) 0%, var(--orange-deep) 100%);
  }
  .back-texture {
    position: absolute; inset: 0 0 70px 0;
    background: radial-gradient(circle at 60% 40%, rgba(252,197,28,.35), rgba(252,197,28,0) 70%);
  }
  .back-brand {
    position: absolute; left: 0; right: 0; top: 48px;
    text-align: center; color: var(--brown); font-weight: 700;
  }
  .back-brand-top { display: flex; align-items: center; justify-content: center; gap: 16px; font-size: 62px; line-height: 1; }
  .back-brand-top .brand-dot { width: 64px; height: 64px; }
  .back-brand-sub { font-size: 32px; line-height: 1.15; margin-top: 6px; }
  .back-band {
    position: absolute; left: 0; right: 0; bottom: 0; height: 70px;
    background: var(--brown);
    display: flex; align-items: center; justify-content: center;
  }
  .back-address { color: var(--yellow); font-weight: 500; font-size: 18px; letter-spacing: .3px; }
</style>
</head>
<body>

<section class="card card-front" aria-label="Business card front">
  <div class="front-brand-zone"></div>
  <div class="front-divider"></div>
  <div class="front-brand">
    <div class="brand-dot"></div>
    <div class="front-brand-name">Bright Ridge<small>General Contractors, Inc.</small></div>
  </div>

  <ul class="contact-list">
    <li class="contact-row">
      <span class="contact-icon"><svg viewBox="0 0 24 24"><circle cx="12" cy="8" r="4.5"/><path d="M3.5 21c0-4.7 3.8-7.5 8.5-7.5s8.5 2.8 8.5 7.5z"/></svg></span>
      <div>
        <div class="person-name">Sam Harlow</div>
        <div class="person-title">Keystone Certified Roof Inspector<br>Licensed Property Adjuster</div>
      </div>
    </li>
    <li class="contact-row">
      <span class="contact-icon"><svg viewBox="0 0 24 24"><path d="M2 5h20v14H2z" fill="none" stroke="#fff" stroke-width="2"/><path d="M2 5l10 8 10-8" fill="none" stroke="#fff" stroke-width="2"/></svg></span>
      <div class="contact-text">sam@<span class="accent">brightridge</span>tx.com</div>
    </li>
    <li class="contact-row">
      <span class="contact-icon"><svg viewBox="0 0 24 24"><path d="M6.6 10.8a15.1 15.1 0 0 0 6.6 6.6l2.2-2.2a1 1 0 0 1 1-.25 11.4 11.4 0 0 0 3.6.57 1 1 0 0 1 1 1V20a1 1 0 0 1-1 1A17 17 0 0 1 3 4a1 1 0 0 1 1-1h3.5a1 1 0 0 1 1 1 11.4 11.4 0 0 0 .57 3.6 1 1 0 0 1-.25 1z"/></svg></span>
      <div class="contact-text"><span class="accent">(555) 014-2200</span><br><span class="label">Mobile/Text:</span> <span class="accent">(555) 019-3781</span></div>
    </li>
  </ul>
</section>

<section class="card card-back" aria-label="Business card back">
  <div class="back-texture" role="img" aria-label="Yellow speckled grunge texture"></div>
  <div class="back-brand">
    <div class="back-brand-top"><span>Bright</span><span class="brand-dot"></span><span>Ridge</span></div>
    <div class="back-brand-sub">General Contractors, Inc.</div>
  </div>
  <div class="back-band">
    <p class="back-address">4410 Cedar Mill Road Suite 118, Fairview, TX 75000</p>
  </div>
</section>

</body>
</html>
```